Rare Glow Edibles Gummies

Packaging design for custom mylars for cannabis infused gummies. I need a space for a warning label, nutrition facts, ingredients, brand logo and then individualized item details. We will later be doing assorted peanut butter cups, hard candies, etc.

```html
<!DOCTYPE html>
<html lang="fr">
<head>
<meta charset="utf-8">
<title>Rare Glow Edibles – Gummies pouch</title>
<link href="https://fonts.googleapis.com/css2?family=Poppins:ital,wght@0,400;0,600;0,700;0,800;1,700&family=Lexend:wght@700&family=Roboto+Condensed:wght@400&display=swap" rel="stylesheet">
<style>
  :root {
    --pouch-purple: #3c0fa3;
    --pouch-edge: #1a0a3c;
    --accent-orange: #ff7f00;
    --text-white: #ffffff;
    --warn-red: #e8343c;
    --page-bg: #ffffff;
  }
  * { box-sizing: border-box; margin: 0; padding: 0; }
  html, body { width: 1200px; height: 1000px; overflow: hidden; background: var(--page-bg); }
  body { position: relative; font-family: "Poppins", sans-serif; }

  .pouch { position: absolute; top: 101px; width: 489px; height: 794px; }
  .pouch--front { left: 83px; }
  .pouch--back { left: 625px; }
  .pouch__shape { position: absolute; inset: 0; width: 100%; height: 100%; }

  .tear-band {
    position: absolute; left: 35px; top: 67px; width: 419px; height: 50px;
    background: var(--accent-orange); border-radius: 10px;
    display: flex; align-items: center; justify-content: center;
  }
  .tear-band__label {
    font-weight: 700; font-size: 24px; color: var(--pouch-purple);
    letter-spacing: 0.2px; background: var(--accent-orange); padding: 0 6px; position: relative; z-index: 1;
  }
  .tear-line {
    position: absolute; left: 0; right: 0; top: 92px; height: 0;
    border-top: 2px dotted var(--text-white); opacity: 0.85;
  }

  /* front */
  .quality-tabs { position: absolute; left: 0; top: 209px; width: 219px; }
  .quality-tab {
    height: 33px; margin-bottom: 2px; border: 1.5px solid var(--text-white);
    border-left: none; border-radius: 0 6px 6px 0;
    font-size: 19px; line-height: 30px; padding-left: 6px; color: var(--text-white); white-space: nowrap;
  }
  .quality-tab--active { background: var(--text-white); color: var(--pouch-purple); }

  .brand-mark { position: absolute; left: 232px; top: 174px; width: 168px; height: 168px;
    border: 1.5px solid var(--text-white); border-radius: 50%; }
  .brand-name {
    position: absolute; left: 240px; top: 228px; width: 240px;
    font-weight: 600; font-size: 27px; line-height: 30px; color: var(--accent-orange); text-align: center;
  }

  .steps { position: absolute; top: 428px; left: 0; width: 100%; font-size: 26px; color: var(--text-white); }
  .steps span { position: absolute; white-space: nowrap; }

  .tagline { position: absolute; left: 15px; top: 508px; font-weight: 700; font-size: 36px; line-height: 46px; }
  .tagline__lead { color: var(--text-white); display: block; }
  .tagline__follow { color: var(--accent-orange); display: block; }

  .pack-facts {
    position: absolute; left: 66px; top: 668px; width: 357px; height: 46px;
    background: var(--accent-orange); border: 1.5px solid var(--text-white); border-radius: 10px;
    display: flex; color: var(--text-white); font-weight: 800; font-size: 20px;
  }
  .pack-facts__weight { width: 230px; border-right: 1.5px solid var(--text-white); display: flex; align-items: center; justify-content: center; }
  .pack-facts__thc { flex: 1; display: flex; align-items: center; padding-left: 11px; }

  /* back */
  .info-title {
    position: absolute; top: 125px; left: 0; width: 100%; text-align: center;
    font-family: "Lexend", sans-serif; font-weight: 700; font-size: 52px; color: var(--text-white);
  }
  .composition {
    position: absolute; left: 12px; top: 216px; width: 464px; height: 147px;
    background: var(--text-white); border-radius: 8px; padding: 20px 12px 0 11px;
    color: var(--pouch-purple); font-size: 15.6px; line-height: 21px;
  }
  .composition__title { font-weight: 700; font-style: italic; }

  .warnings {
    position: absolute; left: 22px; top: 386px; width: 470px;
    color: var(--accent-orange); font-size: 14.6px; line-height: 18.9px; list-style: none; white-space: nowrap;
  }
  .warnings .indent { padding-left: 4px; }

  .pictograms { position: absolute; left: 0; top: 612px; width: 100%; height: 80px; }

  .distributor {
    position: absolute; left: 0; top: 716px; width: 100%; text-align: center;
    font-family: "Roboto Condensed", sans-serif; font-size: 16.5px; line-height: 20px; color: var(--text-white);
  }
</style>
</head>
<body>

<section class="pouch pouch--front" aria-label="Face avant">
  <svg class="pouch__shape" viewBox="0 0 489 794" aria-hidden="true">
    <path d="M0 0 H489 V82 L483 93 L489 104 V794 H0 V104 L6 93 L0 82 Z" fill="var(--pouch-purple)" stroke="var(--pouch-edge)" stroke-width="1.5"/>
  </svg>
  <div class="tear-line"></div>
  <div class="tear-band"><span class="tear-band__label">CUT THE TOP AND RINK</span></div>

  <div class="quality-tabs">
    <div class="quality-tab quality-tab--active">"Classic" quality</div>
    <div class="quality-tab">"Grands crûs" quality</div>
    <div class="quality-tab">"Prestige" quality</div>
  </div>

  <div class="brand-mark" aria-hidden="true"></div>
  <div class="brand-name">Rare Glow<br>Edibles</div>

  <div class="steps">
    <span style="left:40px">1- Shake</span>
    <span style="left:194px">2- eat</span>
    <span style="left:325px">3- Relax</span>
  </div>

  <p class="tagline">
    <span class="tagline__lead">You should just eat,</span>
    <span class="tagline__follow">then you can relax.</span>
  </p>

  <div class="pack-facts">
    <div class="pack-facts__weight">100 G of Gummies</div>
    <div class="pack-facts__thc">no THC</div>
  </div>
</section>

<section class="pouch pouch--back" aria-label="Face arrière">
  <svg class="pouch__shape" viewBox="0 0 489 794" aria-hidden="true">
    <path d="M0 0 H489 V82 L483 93 L489 104 V794 H0 V104 L6 93 L0 82 Z" fill="var(--pouch-purple)" stroke="var(--pouch-edge)" stroke-width="1.5"/>
  </svg>
  <div class="tear-line"></div>
  <div class="tear-band"><span class="tear-band__label">CUT THE TOP AND RINK</span></div>

  <h1 class="info-title">Information</h1>

  <div class="composition">
    <p class="composition__title">Composition :</p>
    <p>fleurs de chanvre séchées ( Cannabis Sativa L) ou (Cannabis Indica) ou hybrides (Cannabis Sativa L et Indica). Variété répertoriée au catalogue européen, destiné à un usage décoratif ou olfactif.</p>
  </div>

  <ul class="warnings">
    <li>-Produit à utiliser en infusion ou en vaporisation, peut</li>
    <li class="indent">provoquer un état de somnolence,</li>
    <li>-NE PAS FUMER.</li>
    <li>-En cas de traitement médical, demander conseil à</li>
    <li class="indent">son médecin traitant.</li>
    <li>-Ne convient pas aux femmes enceintes et/ou allaitantes.</li>
    <li>-Tenir hors de porter des enfants et éloigné des</li>
    <li class="indent">animaux ;</li>
    <li>-Ce produit n’est pas un stupéfiant, il contient moins de 0.2%</li>
    <li class="indent">de tétrahydrocannabinol (THC) en</li>
    <li>-conformité avec les régulations de l’Union Européenne.</li>
  </ul>

  <svg class="pictograms" viewBox="0 0 489 80" aria-label="Pictogrammes : interdit de fumer, déconseillé aux femmes enceintes, interdit aux moins de 18 ans">
    <g transform="translate(107 40)">
      <rect x="-24" y="-4" width="48" height="8" rx="1" fill="var(--text-white)" transform="rotate(-35)"/>
      <rect x="-24" y="-4" width="7" height="8" fill="#222" transform="rotate(-35)"/>
      <circle r="33" fill="none" stroke="var(--warn-red)" stroke-width="6"/>
      <line x1="-23" y1="-23" x2="23" y2="23" stroke="var(--warn-red)" stroke-width="6"/>
    </g>
    <g transform="translate(257 40)">
      <rect x="-10" y="-26" width="20" height="50" rx="9" fill="var(--text-white)" role="img" aria-label="Silhouette de femme enceinte"/>
      <circle r="33" fill="none" stroke="var(--warn-red)" stroke-width="6"/>
      <line x1="-23" y1="-23" x2="23" y2="23" stroke="var(--warn-red)" stroke-width="6"/>
    </g>
    <g transform="translate(382 40)">
      <text x="0" y="14" text-anchor="middle" font-family="Georgia, serif" font-size="38" fill="var(--text-white)">-18</text>
      <circle r="33" fill="none" stroke="var(--warn-red)" stroke-width="6"/>
      <line x1="-23" y1="-23" x2="23" y2="23" stroke="var(--warn-red)" stroke-width="6"/>
    </g>
  </svg>

  <p class="distributor">Distributeur : Bellvane&amp;Co pour Herbier Doux.fr,<br>24 rue des Lilas, 75011 Paris. France.</p>
</section>

</body>
</html>
```